Oil Field Service company needs professional business cards

Looking to clean up our current company business cards and look a little more professional. Harlow Tubular Services is a US based company that services the oil field. We deal with engineers, managers and oil rigs....................................................................................................................................................................................................................................................................................................................................................................................................

Target Market(s)

Oil and Gas professionals

Industry/Entity Type

Oil And Gas

Contact Information for Business Card

See attached photo as example

Font styles to use
Sans Serif

Colors
ec1f27

Requirements
Must have
• Company Logo, Name, Title, Cell, Office, Fax, Email.
• See attached photo
Nice to have
• External CRT, Internal CRT, Casing Crews, Torque Turn, Laydown Machine
Should not have
• Do not introduce any new pictures and keep it professional looking

```html
<!DOCTYPE html>
<html lang="en">
<head>
<meta charset="utf-8">
<title>Harlow Tubular Services – Business Card</title>
<link rel="stylesheet" href="https://fonts.googleapis.com/css2?family=Open+Sans:wght@400;600;700&family=Roboto+Condensed:wght@400&display=swap">
<style>
  :root {
    --brand-red: #ec1f27;
    --slate: #475763;
    --ink: #2b2b2b;
    --paper: #ffffff;
    --backdrop: #4a3236;
  }
  html, body {
    margin: 0;
    padding: 0;
    width: 1200px;
    height: 1200px;
    overflow: hidden;
    background: var(--backdrop);
    font-family: "Open Sans", sans-serif;
  }
  .canvas {
    position: relative;
    width: 1200px;
    height: 1200px;
  }
  .card {
    position: absolute;
    left: 256px;
    width: 688px;
    height: 389px;
    box-shadow: 0 4px 14px rgba(0,0,0,0.35);
    overflow: hidden;
  }
  .card--front { top: 182px; background: var(--paper); }
  .card--back { top: 628px; background: var(--slate); }

  .side-tab {
    position: absolute;
    top: 46px;
    width: 14px;
    height: 296px;
    background: var(--brand-red);
  }
  .side-tab--left { left: 0; border-radius: 0 14px 14px 0; }
  .side-tab--right { right: 0; border-radius: 14px 0 0 14px; }

  .divider {
    position: absolute;
    left: 382px;
    top: 72px;
    width: 2px;
    height: 254px;
    background: linear-gradient(to bottom, transparent, var(--brand-red) 15%, var(--brand-red) 85%, transparent);
  }

  .wordmark {
    position: absolute;
    display: flex;
    align-items: center;
    gap: 12px;
    font-weight: 700;
    line-height: 1.1;
  }
  .wordmark__dot {
    flex: none;
    width: 18px;
    height: 18px;
    border-radius: 50%;
    background: var(--brand-red);
  }
  .wordmark__name { font-size: 29px; letter-spacing: 0.3px; }
  .card--front .wordmark { left: 50px; top: 160px; width: 320px; color: var(--slate); }
  .card--back .wordmark { left: 0; right: 0; top: 162px; justify-content: center; color: var(--paper); }
  .card--back .wordmark__name { font-size: 32px; }

  .contact {
    position: absolute;
    left: 408px;
    top: 104px;
    color: var(--ink);
  }
  .contact__name {
    margin: 0;
    font-size: 25px;
    font-weight: 700;
    color: var(--brand-red);
    line-height: 1.1;
  }
  .contact__title {
    margin: 2px 0 0;
    font-size: 16.5px;
    color: #333;
  }
  .contact__list {
    list-style: none;
    margin: 20px 0 0;
    padding: 0;
    font-size: 16.5px;
  }
  .contact__item {
    display: flex;
    align-items: center;
    gap: 9px;
    height: 23px;
  }
  .contact__item--address { margin-top: 14px; }
  .contact__icon { width: 18px; height: 18px; flex: none; fill: var(--brand-red); }

  .services {
    position: absolute;
    left: 0;
    right: 0;
    top: 345px;
    text-align: center;
    font-family: "Roboto Condensed", sans-serif;
    font-size: 20px;
    color: var(--ink);
  }
  .services__sep { color: var(--brand-red); margin: 0 4px; }
</style>
</head>
<body>
<main class="canvas">

  <section class="card card--front" aria-label="Business card front">
    <div class="side-tab side-tab--left"></div>
    <div class="side-tab side-tab--right"></div>

    <div class="wordmark">
      <span class="wordmark__dot"></span>
      <span class="wordmark__name">Harlow Tubular Services</span>
    </div>

    <div class="divider"></div>

    <div class="contact">
      <h1 class="contact__name">Wade Callister</h1>
      <p class="contact__title">Area Manager</p>
      <ul class="contact__list">
        <li class="contact__item">
          <svg class="contact__icon" viewBox="0 0 24 24" aria-label="Office"><path d="M2 9c0-3 5-5 10-5s10 2 10 5v2h-5V9c-1-1-3-1.5-5-1.5S8 8 7 9v2H2z"/><path d="M6 12l2-3h8l2 3v7H6z M12 12a2.5 2.5 0 1 0 0 5a2.5 2.5 0 1 0 0-5z"/></svg>
          (555) 310-4820
        </li>
        <li class="contact__item">
          <svg class="contact__icon" viewBox="0 0 24 24" aria-label="Cell"><path d="M7 2h10a1 1 0 0 1 1 1v18a1 1 0 0 1-1 1H7a1 1 0 0 1-1-1V3a1 1 0 0 1 1-1zm1 3v13h8V5z"/></svg>
          (555) 472-1963
        </li>
        <li class="contact__item">
          <svg class="contact__icon" viewBox="0 0 24 24" aria-label="Fax"><path d="M7 2h10v5H7z M3 8h18v9h-3v-3H6v3H3z M7 15h10v7H7z"/></svg>
          (555) 310-4875
        </li>
        <li class="contact__item contact__item--address">
          <svg class="contact__icon" viewBox="0 0 24 24" aria-label="Location"><path d="M12 1a8 8 0 0 0-8 8c0 6 8 14 8 14s8-8 8-14a8 8 0 0 0-8-8zm0 11a3 3 0 1 1 0-6a3 3 0 0 1 0 6z"/></svg>
          Fairhollow, OK 73850
        </li>
      </ul>
    </div>

    <p class="services">External CRT<span class="services__sep">|</span>Internal CRT<span class="services__sep">|</span>Casing Crews<span class="services__sep">|</span>Torque Turn<span class="services__sep">|</span>Laydown Machine</p>
  </section>

  <section class="card card--back" aria-label="Business card back">
    <div class="wordmark">
      <span class="wordmark__dot"></span>
      <span class="wordmark__name">Harlow Tubular Services</span>
    </div>
  </section>

</main>
</body>
</html>
```